Letterhead and Envelope for Mental Health Business

I need letterhead and envelope designs that will match my business cards. I am attaching a *.pds file of my business card so it can be matched.

```html
<!DOCTYPE html>
<html lang="en">
<head>
<meta charset="utf-8">
<title>Hale Counseling – Letterhead and Envelope</title>
<link rel="stylesheet" href="https://fonts.googleapis.com/css2?family=Questrial&family=Arimo:wght@700&display=swap">
<style>
  :root {
    --brand-blue: #2c5f94;
    --brand-green: #5a8a2e;
    --paper: #ffffff;
    --backdrop: #e9e7e3;
    --window: #f6f6f6;
    --window-edge: #d9d9d9;
  }
  * { box-sizing: border-box; margin: 0; padding: 0; }
  html, body { width: 1200px; height: 960px; overflow: hidden; }
  body { background: var(--backdrop); position: relative; font-family: "Questrial", sans-serif; }

  .letterhead {
    position: absolute; left: 60px; top: 40px; width: 680px; height: 880px;
    background: var(--paper);
    box-shadow: 0 6px 18px rgba(0,0,0,.18);
  }
  .letterhead-header {
    position: absolute; left: 0; right: 0; top: 0; height: 150px;
    border-bottom: 2px solid var(--brand-blue);
  }
  .letterhead .brand { position: absolute; left: 26px; top: 58px; }
  .letterhead .sender { position: absolute; right: 30px; top: 50px; text-align: right; }
  .letterhead-footer {
    position: absolute; left: 0; right: 0; bottom: 0; height: 118px;
    background: var(--brand-blue);
    display: flex; flex-direction: column; align-items: center; justify-content: center; gap: 5px;
  }

  .brand { display: flex; align-items: center; gap: 10px; }
  .brand-dot { width: 44px; height: 44px; border-radius: 50%; background: var(--brand-blue); }
  .brand-name {
    font-family: "Questrial", sans-serif; color: var(--brand-blue);
    font-size: 26px; line-height: 1; letter-spacing: 1px; text-transform: uppercase;
  }

  .sender-name {
    font-family: "Questrial", sans-serif; color: var(--brand-blue);
    font-size: 26px; letter-spacing: 3px; line-height: 1.1;
  }
  .sender-credentials {
    color: var(--brand-green); font-style: italic; font-size: 13px; letter-spacing: 2px; margin-top: 6px;
  }

  .contact-line {
    font-family: "Arimo", sans-serif; font-weight: 700; color: #fff;
    font-size: 10.5px; letter-spacing: 1.2px; line-height: 1.3;
  }

  .envelope {
    position: absolute; left: 450px; top: 352px; width: 730px; height: 345px;
    background: var(--paper);
    box-shadow: -4px 6px 14px rgba(0,0,0,.25);
  }
  .envelope .brand { position: absolute; left: 22px; top: 34px; }
  .envelope .brand-dot { width: 56px; height: 56px; }
  .envelope .brand-name { font-size: 32px; }
  .envelope .sender { position: absolute; left: 24px; top: 112px; }
  .envelope .sender-name { font-size: 30px; letter-spacing: 3px; }
  .envelope .sender-credentials { font-size: 14px; margin-top: 4px; }
  .address-window {
    position: absolute; left: 432px; top: 85px; width: 245px; height: 132px;
    background: var(--window); border: 1px solid var(--window-edge); border-radius: 8px;
  }
  .envelope-footer {
    position: absolute; left: 0; right: 0; bottom: 0; height: 82px;
    background: var(--brand-blue);
    padding: 10px 0 0 22px;
    display: flex; flex-direction: column; gap: 4px;
  }
</style>
</head>
<body>
  <section class="letterhead">
    <header class="letterhead-header">
      <div class="brand">
        <span class="brand-dot"></span>
        <span class="brand-name">Hale Counseling</span>
      </div>
      <div class="sender">
        <p class="sender-name">Daniel Hale</p>
        <p class="sender-credentials">LMHC, NCC, DCC</p>
      </div>
    </header>
    <footer class="letterhead-footer">
      <p class="contact-line">Cedar Lane 48, 2315 Albany, USA</p>
      <p class="contact-line">555/014-2290</p>
      <p class="contact-line">danielh@halecounselingllc.com</p>
      <p class="contact-line">www.halecounselingllc.com</p>
    </footer>
  </section>

  <section class="envelope">
    <div class="brand">
      <span class="brand-dot"></span>
      <span class="brand-name">Hale Counseling</span>
    </div>
    <div class="sender">
      <p class="sender-name">Daniel Hale</p>
      <p class="sender-credentials">LMHC, NCC, DCC</p>
    </div>
    <div class="address-window"></div>
    <footer class="envelope-footer">
      <p class="contact-line">Cedar Lane 48, 2315 Albany, USA</p>
      <p class="contact-line">555/014-2290</p>
      <p class="contact-line">danielh@halecounselingllc.com</p>
      <p class="contact-line">www.halecounselingllc.com</p>
    </footer>
  </section>
</body>
</html>
```